Stylish Business Card for Modern hair salon

I need a simple business card design using our salon logo and colours that are in the logo. We service clients of all ages but predominantly those in the 18 to 55 age range. We have a young staff and are looking to have a card that will present a modern and clean image that represents who we are. The card should be in black and white same as our logo. Minimal use of other colours is allowed.

Industry/Entity Type

Hair And Beauty

Contact Information for Business Card

The design should have the following information
salon name - TR Hair Studio
address - 2751 Birchfield Rd.E. Mississauga, ON L7P3K2
phone - 905 614-2870
website - trhairexample.ca
instagram - tr.hairstudio
twitter - @TR_HairStudio

Colors
000000
ffffff
474747

Requirements
Must have
• simple design, salon name, address, phone, website, instagram, twitter info
• Back of card should have the following:
• YOUR NEXT APPOINTMENT
• DATE
• TIME
Nice to have
• simple design, clear to see and read,
• predominantly black and white colour, minimal use of other colours is ok
Should not have
• many colours, various fonts

```html
<!DOCTYPE html>
<html lang="en">
<head>
<meta charset="utf-8">
<title>TR Hair Studio – Business Card</title>
<link href="https://fonts.googleapis.com/css2?family=Montserrat:wght@400;500&display=swap" rel="stylesheet">
<style>
  :root {
    --backdrop: #cbcac6;
    --ink: #000000;
    --paper: #ffffff;
    --grey: #474747;
    --pattern: #f1f1f1;
  }
  * { margin: 0; padding: 0; box-sizing: border-box; }
  html, body {
    width: 1200px; height: 960px; overflow: hidden;
    background: var(--backdrop);
    font-family: "Montserrat", sans-serif;
  }
  .card {
    position: absolute; left: 300px;
    width: 600px; height: 340px;
    box-shadow: 0 3px 8px rgba(0,0,0,.25);
  }

  /* Front */
  .card-front { top: 110px; background: var(--ink); color: var(--paper); }
  .brand-name {
    position: absolute; right: 48px; top: 52px;
    font-size: 30px; font-weight: 500; letter-spacing: 2px;
    color: var(--paper);
  }
  .contact-row {
    position: absolute; left: 46px; right: 46px; top: 245px;
    display: flex; justify-content: space-between; align-items: flex-start;
    font-size: 14px; line-height: 20px; letter-spacing: .3px;
  }
  .contact-phone { text-align: center; }
  .contact-phone .label { font-size: 13px; }
  .contact-phone .number { font-size: 18px; font-weight: 500; }
  .social-line { display: flex; align-items: center; gap: 8px; }
  .social-mark { width: 11px; height: 11px; background: var(--paper); display: inline-block; }
  .web-band {
    position: absolute; left: 0; right: 0; top: 296px; height: 30px;
    background: var(--paper); color: var(--ink);
    display: flex; align-items: center; justify-content: center;
    font-size: 14px; font-weight: 500; letter-spacing: 7px; text-transform: uppercase;
  }

  /* Back */
  .card-back { top: 490px; background: var(--paper); color: var(--ink); overflow: hidden; }
  .back-texture {
    position: absolute; inset: 0;
    background: linear-gradient(160deg, var(--paper), var(--pattern) 50%, var(--paper));
  }
  .appointment {
    position: absolute; left: 60px; right: 60px; top: 95px;
  }
  .appointment-title { font-size: 17px; font-weight: 400; letter-spacing: .3px; }
  .appointment-grid {
    margin-top: 10px;
    display: grid; grid-template-columns: 1fr 1fr; column-gap: 18px; row-gap: 26px;
  }
  .field {
    position: relative; height: 34px;
    border-bottom: 1px solid var(--ink);
    display: flex; align-items: flex-end; padding-bottom: 2px;
    font-size: 16px;
  }
  .field .suffix { position: absolute; right: 0; top: 4px; font-size: 11px; }
  .field-offset { margin-top: -38px; }
</style>
</head>
<body>

<section class="card card-front">
  <div class="brand-name">TR HAIR STUDIO</div>
  <div class="contact-row">
    <address class="contact-address" style="font-style:normal">
      2751 BIRCHFIELD RD.E.<br>MISSISSAUGA, ON L7P3K2
    </address>
    <div class="contact-phone">
      <div class="label">CALL US</div>
      <div class="number">905 614-2870</div>
    </div>
    <div class="contact-social">
      <div class="social-line"><span class="social-mark"></span>@TR_HAIRSTUDIO</div>
      <div class="social-line"><span class="social-mark"></span>TR.HAIRSTUDIO</div>
    </div>
  </div>
  <div class="web-band">www.trhairexample.ca</div>
</section>

<section class="card card-back">
  <div class="back-texture" role="img" aria-label="Faint repeating salon name pattern across the card background"></div>
  <div class="appointment">
    <h2 class="appointment-title">YOUR NEXT APPOINTMENT</h2>
    <div class="appointment-grid">
      <div class="field" style="margin-top:28px">DATE:</div>
      <div class="field">DATE:</div>
      <div class="field">TIME:<span class="suffix">AM/PM</span></div>
      <div class="field" style="margin-top:-28px">TIME:<span class="suffix">AM/PM</span></div>
    </div>
  </div>
</section>

</body>
</html>
```